Digital Marketing Website Redesign, modern, fresh, dynamic

Hi there, we would like to freshen up our website and create a new dynamic look. We are a digital marketing agency who specialise in digital transformation in the form of creating websites for appointment bookings. Our clients are service businesses such as hairdressers, dentists and doctors who's patients need to book appointments with them.

Our company name is Plombek with the point being we can help increase your revenue curve by increasing your appointment bookings.

Our services include building the website, creating campaigns to drive traffic, increasing conversions and monitoring and reporting.

We are playing with a tagline of 'Step into your Digital Transformation' as we have a 5 step journey that customers can take with us getting them from zero to full appointment bookings.

Our current website is www.plomnbek-site.example

You can see a draft design that I mocked up on Canva here https://www.drawpadhub.example/design/QXT82LmnB7K/PoWz41kdRtGyvb_sxE_JNq/edit?utm_content=QXT82LmnB7K&utm_campaign=designshare&utm_medium=link2&utm_source=sharebutton

Also attached some other homepage ideas. In regard to photos we are open to ideas.

Please let if you need any more information to provide us with an initial design. Thanks million and I look forward to receiving fantastic designs :)

Marissa Tobler
Plombek

Target Market(s)

Appointment based businesses such as hairdressers, dentists, doctors

Industry/Entity Type

Marketing and Digital

Coding

Coded - Design and coding required

Number of Pages Required

1 page

Colors
0094D4
00A9DD
6FCCEA
C7EBF8
E9F6FB

Requirements
Must have
• Appointment booking CTA
Nice to have
• A website we like https://www.morwenhalbrook.example

```html
<!DOCTYPE html>
<html lang="en">
<head>
<meta charset="utf-8">
<title>Plombek – Step Into Your Digital Transformation</title>
<link href="https://fonts.googleapis.com/css2?family=Abril+Fatface&family=Roboto:wght@400;500;700&display=swap" rel="stylesheet">
<style>
:root{
  --blue:#0094D4;
  --blue-2:#00A9DD;
  --blue-3:#6FCCEA;
  --blue-4:#C7EBF8;
  --blue-5:#E9F6FB;
  --ink:#222;
  --grey:#555;
  --muted:#9a9a9a;
  --dark:#0d0d0d;
  --white:#fff;
}
*{box-sizing:border-box;margin:0;padding:0}
html,body{width:1200px;height:3844px;overflow:hidden}
body{position:relative;background:var(--white);font-family:"Roboto",Arial,sans-serif;color:var(--ink)}
.abs{position:absolute}
.display{font-family:"Abril Fatface",Georgia,serif;font-weight:400;letter-spacing:.5px}

/* nav */
.logo{left:101px;top:34px;font-size:23px;font-weight:700;color:var(--blue)}
.nav{left:406px;top:42px;display:flex;gap:26px;font-size:12px;color:var(--grey)}
.nav .active{color:var(--ink);text-decoration:underline;font-weight:500}
.btn-outline{border:2px solid var(--blue);font-size:11px;font-weight:700;color:var(--ink);display:flex;align-items:center;justify-content:center;letter-spacing:.3px}
.cta-top{left:1007px;top:31px;width:101px;height:36px}

/* hero */
.hero-title{left:98px;top:140px;font-size:67px;line-height:88px}
.hero-title .l1{color:var(--blue)}
.hero-title .l2{color:var(--blue-3)}
.hero-text{left:98px;top:346px;width:700px;font-size:14.5px;font-weight:700;color:#444;line-height:18px}
.hero-photo{left:863px;top:137px;width:244px;height:259px;border-radius:16px;background:linear-gradient(160deg,#f4f4f4,#d9d4cf 60%,#b06a55);box-shadow:0 8px 22px rgba(0,0,0,.12)}

/* stats */
.stat{width:200px;text-align:center;top:500px}
.stat svg{display:block;margin:0 auto}
.stat .num{font-family:"Abril Fatface",Georgia,serif;font-size:38px;color:#555;line-height:38px;margin-top:14px}
.stat .lbl{font-size:11px;color:var(--muted);margin-top:2px}

/* case studies */
.band-blue{left:0;top:713px;width:1200px;height:511px;background:var(--blue)}
.filter{top:795px;height:23px;border:1.5px solid var(--white);color:var(--white);font-size:10px;font-weight:700;display:flex;align-items:center;justify-content:center}
.filter.on{background:var(--white);color:var(--ink)}
.case-title{left:166px;top:820px;font-size:67px;line-height:72px;color:var(--white)}
.case-text{left:163px;top:980px;width:300px;font-size:11px;line-height:19px;color:var(--white)}
.case-btn{left:163px;top:1064px;width:130px;height:35px;border:2px solid var(--white);color:var(--white);font-size:11px;font-weight:700;display:flex;align-items:center;justify-content:center}
.case-img{top:861px;height:281px}

/* pricing */
.plan{top:1334px;width:270px;height:363px;border:1.5px solid var(--blue);border-radius:0 0 14px 14px;padding:16px 30px}
.plan h3{font-family:"Abril Fatface",Georgia,serif;font-weight:400;color:var(--blue);font-size:21px;line-height:22px}
.plan .sub{font-size:10.5px;color:var(--blue-3)}
.plan .price{font-family:"Abril Fatface",Georgia,serif;color:var(--blue);font-size:54px;text-align:center;line-height:60px;margin-top:6px}
.plan .per{font-size:10.5px;color:var(--blue);text-align:right;margin-right:26px;margin-top:-4px}
.plan ul{list-style:none;margin-top:12px}
.plan li{font-size:14px;color:#444;line-height:20px;display:flex;align-items:center;gap:4px}
.plan li.plain{padding-left:16px}
.tick{width:12px;height:12px;flex:none}

/* testimonial */
.quote-band{left:0;top:1800px;width:1200px;height:499px;background:linear-gradient(100deg,#5a4a3c,#3b3733 40%,#2a2a2c 70%,#4b4640)}
.quote-title{left:163px;top:1870px;font-size:65px;line-height:72px;color:var(--white)}
.quote-mark{left:438px;top:2022px;width:28px;height:80px;background:rgba(255,255,255,.25);clip-path:polygon(30% 0,100% 0,60% 100%,0 100%)}
.quote-text{left:473px;top:2020px;width:420px;font-size:16px;line-height:27px;color:var(--white)}
.quote-name{left:473px;top:2134px;display:flex;gap:16px;color:var(--white)}
.quote-name .rule{width:38px;height:2px;background:var(--white);margin-top:10px}
.quote-name b{font-family:"Abril Fatface",Georgia,serif;font-weight:400;font-size:20px;line-height:20px;display:block}
.quote-name span{font-size:11px;font-family:Georgia,serif;font-weight:700}
.dots{left:575px;top:2228px;display:flex;gap:6px}
.dots i{width:5px;height:5px;border-radius:50%;background:var(--white)}
.dots i.on{width:10px;border-radius:3px}

/* digital experience */
.dx-img{left:81px;top:2404px;width:367px;height:356px;background:linear-gradient(135deg,#d8d8d8,#c9b08a 55%,#9a7a4a)}
.dx-card{left:393px;top:2449px;width:204px;height:203px;border-radius:6px;background:linear-gradient(160deg,#f3f3f3,#ddd7d2 55%,#a8584a);box-shadow:0 6px 18px rgba(0,0,0,.15)}
.dx-title{left:643px;top:2430px;font-size:64px;line-height:74px;color:var(--blue)}
.dx-text{left:641px;top:2603px;width:480px;font-size:11px;line-height:19px;color:#555}
.dx-text em{font-style:normal;color:var(--blue);font-weight:500}
.dx-btn{left:641px;top:2683px;width:130px;height:37px}

/* newsletter */
.hello{left:0;top:2848px;width:1200px;text-align:center;font-size:63px;line-height:70px;color:var(--blue)}
.hello-sub{left:0;top:2944px;width:1200px;text-align:center;font-size:20px;color:var(--blue-2);line-height:32px}
.hello-sub b{font-weight:700;color:var(--blue);font-style:italic}
.field{left:387px;top:3057px;width:353px;height:43px;border:1.5px solid var(--blue-3);font-size:10px;color:#777;padding:15px 24px}
.subscribe{left:683px;top:3058px;width:131px;height:38px;background:var(--blue);color:var(--white);font-size:10.5px;font-weight:700;display:flex;align-items:center;justify-content:center}

/* partners */
.partners{left:163px;top:3175px;width:874px;height:277px;background:var(--blue-5)}
.partners-head{left:206px;top:3214px;width:788px;display:flex;align-items:center;gap:10px;font-family:Georgia,serif;font-weight:700;font-size:13px;color:#222;white-space:nowrap}
.partners-head .rule{flex:1;height:1px;background:#bbb}
.brand{display:flex;align-items:center;gap:6px;font-size:22px;font-weight:500;color:#555}
.brand i{width:20px;height:20px;border-radius:50%;background:#555;flex:none}

/* footer */
.footer{left:0;top:3564px;width:1200px;height:280px;background:var(--dark)}
.f-logo{left:163px;top:3616px;font-size:26px;font-weight:700;color:var(--blue)}
.f-text{left:163px;top:3670px;width:210px;font-size:9.5px;line-height:17px;color:#ccc}
.socials{left:163px;top:3750px;display:flex;gap:13px}
.socials i{width:23px;height:23px;background:var(--white)}
.f-col{top:3622px}
.f-col h4{font-size:14px;font-weight:500;color:var(--white);margin-bottom:14px}
.f-col p{font-size:9.5px;color:#ccc;line-height:24px;display:flex;align-items:center;gap:8px}
.copy{left:0;top:3822px;width:1200px;text-align:center;font-size:9.5px;color:#ccc}
</style>
</head>
<body>

<!-- navigation -->
<div class="abs logo">Plombek</div>
<nav class="abs nav">
  <span class="active">Home</span><span>About</span><span>Services</span><span>Case Studies</span><span>Apps</span><span>Pricing</span>
</nav>
<div class="abs btn-outline cta-top">GET START</div>

<!-- hero -->
<h1 class="abs display hero-title"><span class="l1">Step Into Your</span><br><span class="l2">Digital Transformation</span></h1>
<p class="abs hero-text">Digital Transformation Is A Journey. At Plombek We Divide The Journey Into Five Key Steps That Take Your Business From Comprehensive Market Research To Full Appointment Bookings. Ready To Go On That Journey?</p>
<div class="abs hero-photo" role="img" aria-label="Photo of a smiling man in a plaid shirt looking through a magnifying glass"></div>

<!-- stats -->
<div class="abs stat" style="left:146px">
  <svg width="50" height="46" viewBox="0 0 50 46" fill="none" stroke="#666" stroke-width="3"><rect x="3" y="7" width="44" height="36" rx="2"/><line x1="3" y1="16" x2="47" y2="16"/><line x1="14" y1="2" x2="14" y2="11"/><line x1="36" y1="2" x2="36" y2="11"/><polyline points="16,28 23,34 34,22"/></svg>
  <div class="num">762</div><div class="lbl">Appointments Booked</div>
</div>
<div class="abs stat" style="left:369px">
  <svg width="50" height="46" viewBox="0 0 50 46" fill="none" stroke="#666" stroke-width="3"><path d="M6 17h9l22-11v32L15 27H6z"/><path d="M14 27l4 13h6l-3-13"/><path d="M42 16v12"/></svg>
  <div class="num">31</div><div class="lbl">Marketing Companies</div>
</div>
<div class="abs stat" style="left:601px">
  <svg width="50" height="46" viewBox="0 0 50 46" fill="#666"><rect x="2" y="30" width="4" height="12"/><rect x="10" y="18" width="4" height="24"/><rect x="18" y="6" width="4" height="36"/><rect x="26" y="22" width="4" height="20"/><rect x="34" y="14" width="4" height="28"/><rect x="42" y="26" width="4" height="16"/></svg>
  <div class="num">25%</div><div class="lbl">Website Traffic Increase</div>
</div>
<div class="abs stat" style="left:815px;top:490px">
  <svg width="50" height="48" viewBox="0 0 50 48" fill="none" stroke="#666" stroke-width="3"><path d="M25 4a15 15 0 0 0-9 27v6h18v-6a15 15 0 0 0-9-27z"/><line x1="19" y1="43" x2="31" y2="43"/><polyline points="27,12 21,22 29,22 23,32"/></svg>
  <svg width="44" height="22" viewBox="0 0 44 22" fill="none" stroke="#666" stroke-width="3.5" style="margin-top:10px"><path d="M22 11c-5-7-17-8-17 0s12 7 17 0 17-8 17 0-12 7-17 0z"/></svg>
  <div class="lbl" style="margin-top:12px">Creative Ideas</div>
</div>

<!-- case studies -->
<section class="abs band-blue"></section>
<div class="abs filter on" style="left:667px;width:44px">ALL</div>
<div class="abs filter" style="left:727px;width:88px">MARKETING</div>
<div class="abs filter" style="left:831px;width:81px">BRANDING</div>
<div class="abs filter" style="left:927px;width:46px">SEO</div>
<div class="abs filter" style="left:990px;width:47px">WEB</div>
<h2 class="abs display case-title">Our Case<br>Studies</h2>
<p class="abs case-text">Ad Nec Unum Copiosae. Sea Ex Everti Labores, Ad Option Iuvaret Qui. Id Quo Esse Nusquam.</p>
<div class="abs case-btn">VIEW ALL CASES</div>
<div class="abs case-img" style="left:510px;width:303px;background:linear-gradient(160deg,#c99270,#7a4a3a 55%,#3a2a3a)" role="img" aria-label="Photo of a woman taking a selfie surrounded by colourful social media icons"></div>
<div class="abs case-img" style="left:833px;width:303px;background:linear-gradient(160deg,#5f9fb8,#3e7f98 60%,#2d6078)" role="img" aria-label="Photo of a man stepping out of a large phone screen holding clothing"></div>
<div class="abs case-img" style="left:1157px;width:43px;height:278px;border:3px solid #fff;border-right:0;background:linear-gradient(160deg,#e8eef2,#b8c6d0)" role="img" aria-label="Photo of a third case study"></div>

<!-- pricing -->
<div class="abs plan" style="left:146px">
  <h3>Starter Plan</h3><div class="sub">Build A Beautiful Website</div>
  <div class="price">€6,999</div><div class="per">Initial Set Up Fee</div>
  <ul>
    <li><svg class="tick" viewBox="0 0 12 12"><circle cx="6" cy="6" r="6" fill="#0094D4"/><polyline points="3,6 5.2,8 9,4" fill="none" stroke="#fff" stroke-width="1.5"/></svg>Homepage</li>
    <li><svg class="tick" viewBox="0 0 12 12"><circle cx="6" cy="6" r="6" fill="#0094D4"/><polyline points="3,6 5.2,8 9,4" fill="none" stroke="#fff" stroke-width="1.5"/></svg>Landing pages</li>
    <li><svg class="tick" viewBox="0 0 12 12"><circle cx="6" cy="6" r="6" fill="#0094D4"/><polyline points="3,6 5.2,8 9,4" fill="none" stroke="#fff" stroke-width="1.5"/></svg>Usability - platform adaptability</li>
    <li><svg class="tick" viewBox="0 0 12 12"><circle cx="6" cy="6" r="6" fill="#0094D4"/><polyline points="3,6 5.2,8 9,4" fill="none" stroke="#fff" stroke-width="1.5"/></svg>Performance</li>
    <li><svg class="tick" viewBox="0 0 12 12"><circle cx="6" cy="6" r="6" fill="#0094D4"/><polyline points="3,6 5.2,8 9,4" fill="none" stroke="#fff" stroke-width="1.5"/></svg>SEO</li>
    <li><svg class="tick" viewBox="0 0 12 12"><circle cx="6" cy="6" r="6" fill="#0094D4"/><polyline points="3,6 5.2,8 9,4" fill="none" stroke="#fff" stroke-width="1.5"/></svg>Payment gateway</li>
    <li><svg class="tick" viewBox="0 0 12 12"><circle cx="6" cy="6" r="6" fill="#0094D4"/><polyline points="3,6 5.2,8 9,4" fill="none" stroke="#fff" stroke-width="1.5"/></svg>Online booking app</li>
  </ul>
</div>
<div class="abs plan" style="left:465px">
  <h3>Premium Plan</h3><div class="sub">Online Marketing</div>
  <div class="price">€499</div><div class="per">For A Month</div>
  <ul>
    <li><svg class="tick" viewBox="0 0 12 12"><circle cx="6" cy="6" r="6" fill="#0094D4"/><polyline points="3,6 5.2,8 9,4" fill="none" stroke="#fff" stroke-width="1.5"/></svg>Market research</li>
    <li><svg class="tick" viewBox="0 0 12 12"><circle cx="6" cy="6" r="6" fill="#0094D4"/><polyline points="3,6 5.2,8 9,4" fill="none" stroke="#fff" stroke-width="1.5"/></svg>Marketing Campaigns</li>
    <li><svg class="tick" viewBox="0 0 12 12"><circle cx="6" cy="6" r="6" fill="#0094D4"/><polyline points="3,6 5.2,8 9,4" fill="none" stroke="#fff" stroke-width="1.5"/></svg>Conversion Rate Performance</li>
    <li><svg class="tick" viewBox="0 0 12 12"><circle cx="6" cy="6" r="6" fill="#0094D4"/><polyline points="3,6 5.2,8 9,4" fill="none" stroke="#fff" stroke-width="1.5"/></svg>Scalability</li>
    <li><svg class="tick" viewBox="0 0 12 12"><circle cx="6" cy="6" r="6" fill="#0094D4"/><polyline points="3,6 5.2,8 9,4" fill="none" stroke="#fff" stroke-width="1.5"/></svg>Social Compelling content</li>
    <li><svg class="tick" viewBox="0 0 12 12"><circle cx="6" cy="6" r="6" fill="#0094D4"/><polyline points="3,6 5.2,8 9,4" fill="none" stroke="#fff" stroke-width="1.5"/></svg>Get online bookings</li>
    <li><svg class="tick" viewBox="0 0 12 12"><circle cx="6" cy="6" r="6" fill="#0094D4"/><polyline points="3,6 5.2,8 9,4" fill="none" stroke="#fff" stroke-width="1.5"/></svg>GDPR compliance</li>
    <li class="plain">Chat bot / AI integration/ Coach</li>
  </ul>
</div>
<div class="abs plan" style="left:783px;top:1332px">
  <h3>Ultimate Plan</h3><div class="sub">Monitor And Maintain</div>
  <div class="price">€899</div><div class="per">For A Month</div>
  <ul>
    <li><svg class="tick" viewBox="0 0 12 12"><circle cx="6" cy="6" r="6" fill="#0094D4"/><polyline points="3,6 5.2,8 9,4" fill="none" stroke="#fff" stroke-width="1.5"/></svg>Indepth reporting</li>
    <li><svg class="tick" viewBox="0 0 12 12"><circle cx="6" cy="6" r="6" fill="#0094D4"/><polyline points="3,6 5.2,8 9,4" fill="none" stroke="#fff" stroke-width="1.5"/></svg>Customer review</li>
    <li><svg class="tick" viewBox="0 0 12 12"><circle cx="6" cy="6" r="6" fill="#0094D4"/><polyline points="3,6 5.2,8 9,4" fill="none" stroke="#fff" stroke-width="1.5"/></svg>Industry updates</li>
    <li><svg class="tick" viewBox="0 0 12 12"><circle cx="6" cy="6" r="6" fill="#0094D4"/><polyline points="3,6 5.2,8 9,4" fill="none" stroke="#fff" stroke-width="1.5"/></svg>Buying cycle alignment</li>
    <li><svg class="tick" viewBox="0 0 12 12"><circle cx="6" cy="6" r="6" fill="#0094D4"/><polyline points="3,6 5.2,8 9,4" fill="none" stroke="#fff" stroke-width="1.5"/></svg>Digital tools and technologies</li>
  </ul>
</div>

<!-- testimonial -->
<section class="abs quote-band" role="img" aria-label="Dark photo of hands holding a phone showing a booking confirmation over a keyboard and notebook"></section>
<h2 class="abs display quote-title">What People<br>Say</h2>
<div class="abs quote-mark"></div>
<p class="abs quote-text">100 Bookings In First Month!<br>From 55 New Patients Per Month! Plombek's Booking System Helped Us Get Over 100 Appointment Bookings In May 2020.</p>
<div class="abs quote-name"><div class="rule"></div><div><b>Delphine Arvelo</b><span>Owner, Crest &amp; Comb</span></div></div>
<div class="abs dots"><i></i><i></i><i class="on"></i><i></i></div>

<!-- digital experience -->
<div class="abs dx-img" role="img" aria-label="Photo of a woman using a tablet with floating notification icons"></div>
<div class="abs dx-card" role="img" aria-label="Photo of a cheerful man in a plaid shirt pointing"></div>
<h2 class="abs display dx-title">Digital<br>Experience</h2>
<p class="abs dx-text">Step Into The Future Of Digital Excellence With <em>Plombek</em>. Our Blend Of Sleek Design And Advanced Tech Ensures A Smooth And Captivating User Experience. Explore Innovation At Your Fingertips – Welcome To A Redefined Digital Space!</p>
<div class="abs btn-outline dx-btn">DISCOVER MORE</div>

<!-- newsletter -->
<h2 class="abs display hello">Say Hello To Market!</h2>
<p class="abs hello-sub">Sing Up For Newsletter And Receive<br><b>40% Discount On First Project</b></p>
<div class="abs field">Email Address</div>
<div class="abs subscribe">SUBSCRIBE NOW</div>

<!-- partners -->
<section class="abs partners"></section>
<div class="abs partners-head"><span class="rule"></span>OVER 1K+ BUSINESSES GROWING WITH MARKET<span class="rule"></span></div>
<div class="abs brand" style="left:206px;top:3264px"><i></i>Tunewave</div>
<div class="abs brand" style="left:339px;top:3264px">Boxvale</div>
<div class="abs brand" style="left:560px;top:3264px">Searchly</div>
<div class="abs brand" style="left:733px;top:3264px">Staynest</div>
<div class="abs brand" style="left:863px;top:3264px">Marketly</div>
<div class="abs brand" style="left:206px;top:3320px"><i></i>Tunewave</div>
<div class="abs brand" style="left:339px;top:3320px">Boxvale</div>
<div class="abs brand" style="left:560px;top:3320px">Searchly</div>
<div class="abs brand" style="left:733px;top:3320px">Staynest</div>
<div class="abs brand" style="left:863px;top:3320px">Marketly</div>
<div class="abs brand" style="left:206px;top:3376px"><i></i>Tunewave</div>
<div class="abs brand" style="left:339px;top:3376px">Boxvale</div>
<div class="abs brand" style="left:560px;top:3376px">Searchly</div>
<div class="abs brand" style="left:733px;top:3376px">Staynest</div>
<div class="abs brand" style="left:863px;top:3376px">Marketly</div>

<!-- footer -->
<footer class="abs footer"></footer>
<div class="abs f-logo">Plombek</div>
<p class="abs f-text">It is a long established fact that a reader will be distracted by the readable content of a page when looking at its layout</p>
<div class="abs socials"><i></i><i></i><i></i><i></i></div>
<div class="abs f-col" style="left:493px"><h4>Our services</h4><p>SEO Marketing</p><p>SEO Services</p><p>Pay Per Click</p><p>Social Media</p><p>SEO Audit</p></div>
<div class="abs f-col" style="left:703px"><h4>Quick link</h4><p>Home</p><p>About Us</p><p>Main Services</p><p>Pricing</p><p>Our Cases</p></div>
<div class="abs f-col" style="left:896px"><h4>Contact us</h4>
  <p><svg width="10" height="12" viewBox="0 0 10 12" fill="none" stroke="#fff" stroke-width="1.3"><path d="M5 11S1 7 1 4.5a4 4 0 0 1 8 0C9 7 5 11 5 11z"/><circle cx="5" cy="4.5" r="1.3"/></svg>48 Harlow Lane, Brookfield</p>
  <p><svg width="11" height="9" viewBox="0 0 11 9" fill="none" stroke="#fff" stroke-width="1.2"><rect x=".6" y=".6" width="9.8" height="7.8"/><polyline points=".6,.6 5.5,5 10.4,.6"/></svg>hello@plombek-mail.example</p>
  <p><svg width="11" height="9" viewBox="0 0 11 9" fill="none" stroke="#fff" stroke-width="1.2"><rect x=".6" y=".6" width="9.8" height="7.8"/><polyline points=".6,.6 5.5,5 10.4,.6"/></svg>+1 (555) 014-2270</p>
</div>
<div class="abs copy">Copyright © 2024 <span style="color:#fff">Market</span>. All Rights Reserved.</div>

</body>
</html>
```